Brivora Australia Company Values.

We have just completed our company purpose, beliefs and values (for the first time, we have not had these before)
We are now wanting to add images to each company value as a visual
so they are easily identified and understood for all our staff - we need them to remember the 5 Values.
We are a manufacturer of dental materials and infection control products, based in Melbourne.

What we would like:
- A Poster (that can be placed in our staff lunch rooms)
- The values to be lined up Horizontally
- Image on the top of the words
- Wording does not all need to be the same text font
- No image photographs - please use image graphics
- No images with people
- No dental related graphics

Target audience: Brivora staff

Our Values are:
Think Big
Have a go, learn and adapt
If you're gonna do it, do it bloody well
Empower Others
Be a good human

I have uploaded some examples.

Target Market(s)

Brivora Team members

Industry/Entity Type

Healthcare

Colors

Designer to choose colors to be used in the design.

Requirements
Must have
• Clear horizontal layout, space between each value
Should not have
• No images with humans or dental

```html
<!DOCTYPE html>
<html lang="en">
<head>
<meta charset="utf-8">
<title>Brivora Australia – Company Values</title>
<link rel="stylesheet" href="https://fonts.googleapis.com/css2?family=Fira+Sans:wght@400;500;600;700;800;900&family=Fira+Sans+Condensed:wght@900&family=Fira+Sans+Extra+Condensed:wght@300;900&display=swap">
<style>
  :root{
    --paper:#ffffff;
    --white:#ffffff;
    /* bright set */
    --think-bg:#0019f0; --think-accent:#22e4ff; --think-icon:#9ff3ff;
    --try-bg:#ffcb2e;   --try-accent:#f0420f;   --try-icon:#f26a1a;
    --well-bg:#3c0a96;  --well-accent:#b7b4ff;  --well-icon:#9d9cf0;
    --empower-bg:#ff0a7f; --empower-accent:#ffc3e6; --empower-icon:#ffd0ea;
    --human-bg:#00e676; --human-accent:#0b5a36; --human-icon:#1a7a45;
    /* deep set */
    --think-bg-2:#1a0f7a; --think-accent-2:#1e8fff; --think-icon-2:#62c6ff;
    --try-bg-2:#ff9a00;   --try-accent-2:#b53b05;  --try-icon-2:#c74408;
    --well-bg-2:#7a0ce0;  --well-accent-2:#d8c8ff; --well-icon-2:#c6b4ff;
    --empower-bg-2:#ff0a5a; --empower-accent-2:#ffc7d8; --empower-icon-2:#ffd3df;
    --human-bg-2:#8ee800; --human-accent-2:#146a2a; --human-icon-2:#2f8a2a;
  }
  *{margin:0;padding:0;box-sizing:border-box}
  html,body{width:1200px;height:849px;overflow:hidden;background:var(--paper)}
  .poster{position:relative;width:1200px;height:849px}
  .values-row{position:absolute;left:0;display:grid;grid-template-columns:repeat(5,minmax(0,1fr));width:1191px;height:411px}
  .values-row--bright{top:0}
  .values-row--deep{top:432px}
  .value{position:relative;min-width:0;overflow:hidden;display:flex;flex-direction:column;align-items:center;
    font-family:"Fira Sans",sans-serif;color:var(--white);text-align:center;line-height:.92;background:var(--bg)}
  .value__icon{margin-top:28px;width:150px;height:150px;border-radius:22px;background:var(--icon);opacity:.85;flex:none}
  .value__words{margin-top:40px;display:flex;flex-direction:column;align-items:center;font-weight:inherit}
  .value__words span{display:block;white-space:nowrap}
  .value--think{--bg:var(--think-bg);--accent:var(--think-accent);--icon:var(--think-icon)}
  .value--try{--bg:var(--try-bg);--accent:var(--try-accent);--icon:var(--try-icon)}
  .value--well{--bg:var(--well-bg);--accent:var(--well-accent);--icon:var(--well-icon)}
  .value--empower{--bg:var(--empower-bg);--accent:var(--empower-accent);--icon:var(--empower-icon)}
  .value--human{--bg:var(--human-bg);--accent:var(--human-accent);--icon:var(--human-icon)}
  .values-row--deep .value--think{--bg:var(--think-bg-2);--accent:var(--think-accent-2);--icon:var(--think-icon-2)}
  .values-row--deep .value--try{--bg:var(--try-bg-2);--accent:var(--try-accent-2);--icon:var(--try-icon-2)}
  .values-row--deep .value--well{--bg:var(--well-bg-2);--accent:var(--well-accent-2);--icon:var(--well-icon-2)}
  .values-row--deep .value--empower{--bg:var(--empower-bg-2);--accent:var(--empower-accent-2);--icon:var(--empower-icon-2)}
  .values-row--deep .value--human{--bg:var(--human-bg-2);--accent:var(--human-accent-2);--icon:var(--human-icon-2)}

  .think__small{font-weight:900;font-size:64px;color:var(--accent);letter-spacing:-1px}
  .think__big{font-family:"Fira Sans Condensed",sans-serif;font-weight:900;font-size:126px;margin-top:6px;letter-spacing:-1px}

  .try__line{font-weight:800;font-size:40px;color:var(--accent);letter-spacing:-1px;margin-bottom:8px}
  .try__line--learn{font-weight:500;font-size:42px}
  .try__big{font-weight:900;font-size:68px;letter-spacing:-1px;margin-top:2px}

  .well__lead{font-weight:400;font-size:38px;color:var(--accent)}
  .well__small{font-weight:700;font-size:19px;color:var(--accent);margin:6px 0 8px}
  .well__bold{font-weight:900;font-size:46px}
  .well__big{font-weight:700;font-size:68px;margin-top:2px}

  .empower__big{font-family:"Fira Sans Extra Condensed",sans-serif;font-weight:900;font-size:100px;transform:scaleX(.6);margin-top:-4px}
  .empower__light{font-family:"Fira Sans Extra Condensed",sans-serif;font-weight:300;font-size:92px;color:var(--accent);transform:scaleX(.8);margin-top:-6px}

  .human__lead{font-weight:500;font-size:66px;color:var(--accent);letter-spacing:-1px}
  .human__big{font-weight:900;font-size:64px;margin:4px 0 6px}
  .human__tail{font-weight:600;font-size:46px;color:var(--accent)}
</style>
</head>
<body>
<main class="poster">
  <section class="values-row values-row--bright" aria-label="Brivora Australia company values">
    <article class="value value--think">
      <div class="value__icon" role="img" aria-label="Icon: brain inside a glowing light bulb"></div>
      <h2 class="value__words"><span class="think__small">THINK</span><span class="think__big">BIG</span></h2>
    </article>
    <article class="value value--try">
      <div class="value__icon" role="img" aria-label="Icon: paper plane flying above an aeroplane"></div>
      <h2 class="value__words"><span class="try__line">HAVE A GO,</span><span class="try__line try__line--learn">LEARN &amp;</span><span class="try__big">ADAPT</span></h2>
    </article>
    <article class="value value--well">
      <div class="value__icon" role="img" aria-label="Icon: magnifying glass over a grid of blocks"></div>
      <h2 class="value__words"><span class="well__lead">IF YOU'RE</span><span class="well__small">GONNA DO IT, DO IT</span><span class="well__bold">BLOODY</span><span class="well__big">WELL</span></h2>
    </article>
    <article class="value value--empower">
      <div class="value__icon" role="img" aria-label="Icon: four hands joined in a circle"></div>
      <h2 class="value__words"><span class="empower__big">EMPOWER</span><span class="empower__light">OTHERS</span></h2>
    </article>
    <article class="value value--human">
      <div class="value__icon" role="img" aria-label="Icon: open hand holding a young plant"></div>
      <h2 class="value__words"><span class="human__lead">BE A</span><span class="human__big">GOOD</span><span class="human__tail">HUMAN</span></h2>
    </article>
  </section>

  <section class="values-row values-row--deep" aria-label="Brivora company values, deep colour version">
    <article class="value value--think">
      <div class="value__icon" role="img" aria-label="Icon: brain inside a glowing light bulb"></div>
      <h2 class="value__words"><span class="think__small">THINK</span><span class="think__big">BIG</span></h2>
    </article>
    <article class="value value--try">
      <div class="value__icon" role="img" aria-label="Icon: paper plane flying above an aeroplane"></div>
      <h2 class="value__words"><span class="try__line">HAVE A GO,</span><span class="try__line try__line--learn">LEARN &amp;</span><span class="try__big">ADAPT</span></h2>
    </article>
    <article class="value value--well">
      <div class="value__icon" role="img" aria-label="Icon: magnifying glass over a grid of blocks"></div>
      <h2 class="value__words"><span class="well__lead">IF YOU'RE</span><span class="well__small">GONNA DO IT, DO IT</span><span class="well__bold">BLOODY</span><span class="well__big">WELL</span></h2>
    </article>
    <article class="value value--empower">
      <div class="value__icon" role="img" aria-label="Icon: four hands joined in a circle"></div>
      <h2 class="value__words"><span class="empower__big">EMPOWER</span><span class="empower__light">OTHERS</span></h2>
    </article>
    <article class="value value--human">
      <div class="value__icon" role="img" aria-label="Icon: open hand holding a young plant"></div>
      <h2 class="value__words"><span class="human__lead">BE A</span><span class="human__big">GOOD</span><span class="human__tail">HUMAN</span></h2>
    </article>
  </section>
</main>
</body>
</html>
```